Tech Laundry service company looking for a new modern and clean web site

Our site is www.brisklinenhub.com we are looking to rebrand our whole website.

We offer free pickup and delivery for laundry and dry cleaning in the NYC area. we target residential customers.

Sites to compare are www.trypolvex.com and www.zentumo.com
Most content can be found at www.brisklinenhub.com

We are looking for a clean and modern look. Nothing to busy

colors and font we use are
Logo font: Harabara
Slogan font: Swiss 721 Light Extended BT

Dark blue: C 100 M 88 Y 0 K 0
Light blue: C 85 M 50 Y 0 K 0
Orange: C 0 M 80 Y 95 K 0

Violet: C 85 M 100 Y 0 K 0

We use only Marlo, Quilse and vendrax
We are provide eco-friendly
next day laundry service

Our mission Statement is to deliver the Cleanest and Brightest clothes in the market. we use only top of the line

"We are the #1 proud supporter of Marlo and Quilse"

There will be 4 pages
the home page
and a 2 page scheduling page

THE HOME PAGE-
navigation bar must include

Home,
Clean my Clothes (schedule a pickup)
Pricing
Blog
Service Area
Commercial/Wholesale
Sign in
must have key elements about our business such as:
1. Our Price is 1.10 a lb
2. "New customers get 50% off first order and 100% off second order!"
3. we have next day service on all laundry orders
Again, you can pull the content off our current website brisklinenhub.com

Order Page-

Attached please find 5 steps of the ordering page. We are looking to condense into 2
we want step2+step3+step4 on one page
then step1+step5 on the second page on step5 we want the coinbird logo attached as well (as we do all credit card processing through CoinBird)
at the end of the process we want to offer them to create a password to auto register
the order confirmation is attached as well. we need all that info but would like it to seem cleaner and modern.

PRICING PAGE-

Wash and Fold 1.10 per Lb ($27 min charge)
Blankets $12 and up
Bathroom Rugs $5.00 and up

Dry Cleaning
Launder and Press shirt 1.25
Suit Jacket 6.00
Pants and Skirts 6.00
2 pc suit 12.00
Dress 10.00 and up
Blouses & Sweaters 6.00

Again, we are looking for a clean and sleek site not to busy.

Based on this we will be needed another 6-8 pages of design work that will be negotiated with the winner at the end of this contest.
Good Luck!

Target Market(s)

our customers are between the ages of 22-40 years old all live in NYC

Industry/Entity Type

Dry Cleaning

Number of Pages Required

4 page

Font styles to use
Other font styles liked:
• Harabara

Requirements
Must have
• sleek and cool design
• see www.polvex.com and zentumo.com for concept
• Our current site is brisklinenhub.com which we are looking to rebrand
Nice to have
• colors and font we use are
• Logo font: Harabara
• Slogan font: Swiss 721 Light Extended BT
• Dark blue: C 100 M 88 Y 0 K 0
• Light blue: C 85 M 50 Y 0 K 0
• Orange: C 0 M 80 Y 95 K 0
• Violet: C 85 M 100 Y 0 K 0
Should not have
• we want all the colors to be uniform. we are sending a message that we are the brightest and cleanest laundry service in the city!

```html
<!DOCTYPE html>
<html lang="en">
<head>
<meta charset="utf-8">
<title>Brisk Linen Hub – Home</title>
<link href="https://fonts.googleapis.com/css2?family=Arimo:wght@400;700&family=Open+Sans:ital,wght@0,400;0,600;0,700;1,400&display=swap" rel="stylesheet">
<style>
:root{
  --navy:#1f3f8f;
  --navy-deep:#14307a;
  --orange:#f0562a;
  --gray-band:#e6e9ef;
  --ink:#333;
  --muted:#666;
  --white:#fff;
}
*{margin:0;padding:0;box-sizing:border-box}
html,body{width:1000px;height:1200px;overflow:hidden;background:var(--white)}
body{position:relative;font-family:"Open Sans",Arial,sans-serif;color:var(--ink)}
.abs{position:absolute}
.heading{font-family:"Arimo",Arial,sans-serif;font-weight:700;letter-spacing:1px;text-transform:uppercase}

/* top bar */
.topbar{left:268px;top:0;width:466px;height:17px;background:var(--navy)}
.topbar-text{top:5px;font-size:5.5px;color:var(--white)}
.social{top:4px;width:8px;height:8px;border-radius:50%;background:var(--white)}

/* header */
.logo{left:300px;top:24px;display:flex;align-items:center;gap:5px}
.logo-mark{width:14px;height:14px;border-radius:50%;background:var(--navy)}
.logo-name{font-size:10px;font-weight:700;color:var(--navy)}
.nav{left:456px;top:27px;width:246px;display:flex;justify-content:space-between;font-size:5.6px;font-weight:700;color:var(--navy);border-bottom:1px solid var(--navy);padding-bottom:3px}
.nav .active{position:relative}
.nav .active::after{content:"";position:absolute;left:0;right:0;bottom:-4px;height:2px;background:var(--orange)}

/* hero */
.hero{left:268px;top:47px;width:466px;height:210px;background:linear-gradient(90deg,#8e969f 0%,#b7bcc2 28%,#6f7f9e 55%,#2f4f93 85%,#27468c 100%)}
.hero-title{left:460px;top:102px;width:250px;font-size:13px;line-height:19px;color:var(--white);letter-spacing:.3px;white-space:nowrap}
.hero-text{left:468px;top:150px;width:230px;font-size:7px;line-height:9px;color:#e8ecf5;text-align:center}
.btn{left:593px;top:191px;width:105px;height:19px;background:var(--orange);color:var(--white);font-size:11px;text-align:center;line-height:19px;letter-spacing:.5px}
.dot{top:241px;width:5px;height:5px;border-radius:50%;background:#c9cfd9}

/* tagline */
.tagline{left:268px;top:268px;width:466px;text-align:center;font-size:10.5px;color:var(--navy);letter-spacing:.9px;white-space:nowrap}

/* features */
.feature{top:308px;width:100px;text-align:center}
.feature svg{display:block;margin:0 auto}
.feature-title{margin-top:8px;font-family:"Arimo",Arial,sans-serif;font-size:7px;color:var(--navy);letter-spacing:.5px}
.feature-text{margin:3px auto 0;width:62px;font-size:6px;line-height:7.3px;color:var(--ink)}
.feature-text .accent{color:var(--orange);font-weight:700}

/* bands */
.band{left:268px;width:466px;background:var(--gray-band)}
.section-title{font-size:11px;color:var(--navy);letter-spacing:1px}
.section-sub{font-size:7px;font-weight:700;color:#111}
.bullets{font-size:6px;line-height:7.5px;color:var(--ink);list-style:disc}
.photo{border-radius:2px}

/* cards */
.card{top:740px;width:191px;height:115px;border:1px solid #9aa1ad;background:var(--white)}
.card-head{height:18px;background:var(--orange);color:var(--white);font-family:"Arimo",Arial,sans-serif;font-weight:700;font-size:7.3px;text-align:center;line-height:18px;letter-spacing:.3px}
.card-body{padding:12px 10px 0 11px;font-size:5.8px;line-height:7.2px;color:var(--muted)}

/* customers */
.customers-title{left:268px;top:879px;width:466px;text-align:center;font-size:10.5px;color:var(--orange)}
.client{top:916px;display:flex;align-items:center;gap:4px;font-family:"Open Sans",Arial,sans-serif;font-weight:700;font-size:8px;color:#555;white-space:nowrap}
.client i{display:block;width:11px;height:11px;border-radius:50%;background:#8a8a8a}

/* join + testimonial */
.join-title{left:300px;top:970px;width:200px;text-align:center;font-size:7px;color:var(--orange);letter-spacing:.2px}
.join-text{left:316px;top:988px;width:168px;text-align:center;font-size:6.2px;line-height:7.7px;color:#222}
.testimonial{left:520px;top:965px;width:176px;height:100px;background:var(--gray-band)}
.testimonial-title{left:527px;top:970px;font-size:7px;color:var(--orange)}
.quote{left:532px;top:1008px;width:156px;text-align:center;font-size:6.2px;line-height:7.6px;font-style:italic;color:#222}
.arrows{left:672px;top:1051px;font-size:7px;color:#777;letter-spacing:4px}

/* footer */
.footer{left:268px;top:1082px;width:466px;height:118px;background:var(--navy)}
.footer-links{left:309px;top:1092px;font-size:7.3px;line-height:8.7px;color:var(--white);list-style:none}
.contact-title{left:518px;top:1092px;font-size:9.5px;font-weight:700;color:var(--white)}
.contact{left:518px;top:1113px;font-size:7px;line-height:8.5px;color:var(--white)}
.footer-social{top:1092px;width:9px;height:9px;border-radius:50%;background:var(--white)}
.footer-rule{left:288px;top:1169px;width:426px;height:1px;background:#5b74b3}
.copyright{left:268px;top:1178px;width:466px;text-align:center;font-size:6.2px;line-height:8px;color:var(--white)}
</style>
</head>
<body>

<!-- top bar -->
<div class="abs topbar"></div>
<div class="abs topbar-text" style="left:611px">(555) 013-2841</div>
<div class="abs topbar-text" style="left:652px">SIGN IN</div>
<span class="abs social" style="left:678px"></span>
<span class="abs social" style="left:687px"></span>
<span class="abs social" style="left:696px"></span>

<!-- header -->
<div class="abs logo"><span class="logo-mark"></span><span class="logo-name">brisklinenhub.com</span></div>
<nav class="abs nav">
  <span class="active">HOME</span><span>CLEAN MY CLOTHES</span><span>PRICING</span><span>BLOG</span><span>SERVICE AREA</span><span>COMMERCIAL/WHOLESALE</span>
</nav>

<!-- hero -->
<div class="abs hero" role="img" aria-label="Photo of a row of front-loading washing machines in a laundromat"></div>
<h1 class="abs heading hero-title">Best rated commercial and<br>residential laundry service</h1>
<p class="abs hero-text">Lorem ipsum dolor sit amet, consectetuer adipiscing elit. Aenean commodo ligula eget dolor. Aenean massa. Cum sociis natoque penatibus et magnis dis parturient montes, nascetur ridiculus mus. Donec quam felis, ultricies nec.</p>
<div class="abs btn">GET STARTED</div>
<span class="abs dot" style="left:679px"></span>
<span class="abs dot" style="left:687px;background:#fff"></span>
<span class="abs dot" style="left:695px"></span>

<!-- tagline -->
<h2 class="abs heading tagline">"We are the #1 proud supporter of Marlo and Quilse"</h2>

<!-- features -->
<div class="abs feature" style="left:323px">
  <svg width="46" height="46" viewBox="0 0 46 46"><circle cx="23" cy="23" r="22" fill="#f0562a"/><circle cx="23" cy="23" r="18" fill="none" stroke="#fff" stroke-width="1.5"/>
    <g fill="none" stroke="#fff" stroke-width="1.5"><rect x="13" y="19" width="13" height="10"/><path d="M26 22h5l3 4v3h-8"/><circle cx="17" cy="30" r="2"/><circle cx="30" cy="30" r="2"/><circle cx="18" cy="18" r="4"/><path d="M18 16v2h2"/></g></svg>
  <div class="feature-title">Next Day Delivery</div>
  <p class="feature-text">Astonishing fast service, ready in 24 hours from pickup time, delivered to your doorsteps.</p>
</div>
<div class="abs feature" style="left:456px">
  <svg width="46" height="46" viewBox="0 0 46 46"><circle cx="23" cy="23" r="22" fill="#f0562a"/><circle cx="23" cy="23" r="18" fill="none" stroke="#fff" stroke-width="1.5"/>
    <g fill="none" stroke="#fff" stroke-width="1.5"><rect x="13" y="19" width="13" height="10"/><path d="M26 22h5l3 4v3h-8"/><circle cx="17" cy="30" r="2"/><circle cx="30" cy="30" r="2"/><circle cx="19" cy="18" r="4"/></g><text x="19" y="20" font-size="5" fill="#fff" text-anchor="middle" font-family="Arial">$</text></svg>
  <div class="feature-title">Free Pickup &amp; Delivery</div>
  <p class="feature-text">We mean it, everything included in the same price, our drivers are out in the city from <span class="accent">9AM to 7PM.</span></p>
</div>
<div class="abs feature" style="left:591px">
  <svg width="46" height="46" viewBox="0 0 46 46"><circle cx="23" cy="23" r="22" fill="#f0562a"/><circle cx="23" cy="23" r="18" fill="none" stroke="#fff" stroke-width="1.5"/><text x="23" y="29" font-size="17" fill="#fff" text-anchor="middle" font-family="Arial">$</text></svg>
  <div class="feature-title">Only $1.10 a Pound?</div>
  <p class="feature-text">Yes and that also includes high quality, on time service and great customer service, we believe its time to make a difference.</p>
</div>

<!-- service features -->
<section class="abs band" style="top:436px;height:144px"></section>
<h2 class="abs heading section-title" style="left:330px;top:464px">Service Features</h2>
<h3 class="abs section-sub" style="left:330px;top:491px">Convenient Laundry Service</h3>
<ul class="abs bullets" style="left:350px;top:509px">
  <li>24 Hour Turnaround.</li><li>Free Pickup and Delivery</li><li>Easy Online Access.</li>
</ul>
<div class="abs photo" style="left:505px;top:452px;width:150px;height:110px;background:linear-gradient(135deg,#d9c28a 0%,#e7a848 35%,#c73a3a 55%,#5a78b8 75%,#8a6a3a 100%);opacity:.85" role="img" aria-label="Illustration of folded towels, a clothes iron and a basket of colourful laundry"></div>

<!-- peace of mind -->
<div class="abs photo" style="left:315px;top:585px;width:95px;height:135px;background:linear-gradient(180deg,#f4f4f4 0%,#d8a56a 40%,#c9a060 70%,#e8e0d4 100%)" role="img" aria-label="Photo of a smiling woman holding a stack of folded clothes"></div>
<h2 class="abs heading section-title" style="left:439px;top:614px">Peace of Mind</h2>
<h3 class="abs section-sub" style="left:439px;top:641px">Quality Assurance</h3>
<p class="abs" style="left:439px;top:658px;width:250px;font-size:6px;line-height:7.5px;color:var(--muted)">Every piece of laundry is handle with care by our trained attendants, we guarantee our service by double checking you wont have any missing clothes before delivery.</p>

<!-- cards -->
<article class="abs card" style="left:301px">
  <div class="card-head">A Customized Commercial Laundry Service</div>
  <p class="card-body">Our superior commercial laundry service is available for hotels, restaurants and a whole range of commercial customers. Among our past clients are Norvale, Avenra, Gridlane, Tessory, and Calloway Bros. Circus. Your laundry will be custom washed according to your preferences as well as professionally folded. All of our laundry is checked for quality assurance so that your business can maintain its high standards. If you're looking for a quality hotel or restaurant laundry service, come to Brisk Linen Hub!</p>
</article>
<article class="abs card" style="left:512px">
  <div class="card-head">Laundry Pickup and Delivery 7 Days a Week</div>
  <p class="card-body">Laundry pickup and delivery shouldn't be a hassle. That's why we accept order online 24/7! The drivers at Brisk Linen Hub are on the road from 9am to 7pm to take care of our commitment of next day delivery. The service doesn't end here – if you have any questions or concerns, our superb customer service staff will address them immediately. When you come to Brisk Linen Hub, you're getting the best of the best in residential and commercial NYC laundry service.</p>
</article>

<!-- customers -->
<section class="abs band" style="top:864px;height:85px"></section>
<h2 class="abs heading customers-title">Some of our customers</h2>
<div class="abs client" style="left:336px"><i></i>Norvale</div>
<div class="abs client" style="left:398px">Avenra</div>
<div class="abs client" style="left:474px"><i></i>Gridlane</div>
<div class="abs client" style="left:536px"><i></i>Tessory</div>
<div class="abs client" style="left:600px">Calloway Bros.</div>

<!-- join + testimonial -->
<h2 class="abs heading join-title">Join thousands of satisfied New Yorkers</h2>
<div class="abs join-text">
  <p>Brisk Linen Hub is NYC Laundry Delivery service at its best. Founded in 2008, our business has expanded to six locations and serves all of Manhattan! We offer free laundry delivery service for a set price of $1.10 per pound for residential and commercial customers.</p>
  <p style="margin-top:7px">We also offer dry-cleaning services at great prices. You can call or schedule a pickup online and we'll pick it up on the same day. You won't find a laundry delivery service that's better than that!</p>
</div>
<aside class="abs testimonial"></aside>
<h2 class="abs heading testimonial-title">Testimonials</h2>
<p class="abs quote">"The detergent that you guys use smells so good!, I've gotten complements on the smell!"<br>Corinne - Manhattan</p>
<div class="abs arrows">‹ ›</div>

<!-- footer -->
<footer class="abs footer"></footer>
<ul class="abs footer-links">
  <li>Home</li><li>Clean My Clothes</li><li>Pricing</li><li>Blog</li><li>Service Area</li><li>Commercial/Wholesale</li><li>Terms of Services</li>
</ul>
<h2 class="abs contact-title">Contact Us</h2>
<div class="abs contact">Brisk Linen Hub<br>t: (555) 013-2841<br>a: 48 Harbor Lane, NY, NY, 10005, USA<br>e: orders@brisklinenhub.com</div>
<span class="abs footer-social" style="left:668px"></span>
<span class="abs footer-social" style="left:681px"></span>
<span class="abs footer-social" style="left:694px"></span>
<div class="abs footer-rule"></div>
<div class="abs copyright">© 2015 All Rights Reserved.<br>brisklinenhub.com</div>

</body>
</html>
```